Wagely Allies Business Card Design

We need a business card designed around our new logo. The business card should be modern in design & should communicate success, confidence, power, sophistication. The target market is young business professionals. This is for a human resource & payroll outsourcing business.

```html
<!DOCTYPE html>
<html lang="en">
<head>
<meta charset="utf-8">
<title>Wagely Allies Business Card</title>
<link rel="stylesheet" href="https://fonts.googleapis.com/css2?family=Poppins:wght@600&family=Questrial&display=swap">
<style>
  :root {
    --page-bg: #5e5e5e;
    --card-bg: #070708;
    --accent-red: #e3212b;
    --text-white: #f2f2f2;
    --rule-red: #8c1118;
  }
  * { box-sizing: border-box; margin: 0; padding: 0; }
  html, body {
    width: 1200px; height: 1200px; overflow: hidden;
    background: var(--page-bg);
  }
  .canvas {
    position: relative; width: 1200px; height: 1200px;
  }
  .card {
    position: absolute; left: 60px; top: 285px;
    width: 1080px; height: 630px;
    background: var(--card-bg);
    border-radius: 42px;
    font-family: "Questrial", "Century Gothic", sans-serif;
    color: var(--text-white);
  }
  .accent-bar {
    position: absolute; left: 64px; top: 126px;
    width: 6px; height: 80px; background: var(--accent-red);
  }
  .accent-line {
    position: absolute; left: 66px; top: 206px;
    width: 2px; height: 322px; background: var(--rule-red);
  }
  .person-name {
    position: absolute; left: 99px; top: 118px;
    font-family: "Poppins", "Century Gothic", sans-serif;
    font-weight: 600; font-size: 38px; line-height: 1;
    color: var(--accent-red); letter-spacing: 0.5px;
  }
  .person-title {
    position: absolute; left: 99px; top: 164px;
    font-size: 29px; line-height: 1;
  }
  .contact-item {
    position: absolute; left: 99px;
    font-size: 25px; line-height: 33px;
  }
  .contact-icon {
    position: absolute; left: 56px;
    width: 22px; height: 22px;
  }
  .address { top: 286px; }
  .icon-pin { top: 308px; }
  .phone { top: 386px; }
  .icon-phone { top: 392px; }
  .mobile { top: 426px; }
  .icon-mobile { top: 432px; }
  .email { top: 466px; }
  .icon-email { top: 472px; }
  .web { top: 506px; }
  .icon-web { top: 512px; }
  .web .domain { color: var(--accent-red); }
  .brand-name {
    position: absolute; right: 70px; top: 128px;
    font-size: 58px; line-height: 1;
    color: var(--text-white); letter-spacing: 0.5px;
  }
</style>
</head>
<body>
<div class="canvas">
  <div class="card">
    <div class="accent-bar"></div>
    <div class="accent-line"></div>

    <div class="person-name">Marten Hale</div>
    <div class="person-title">General Manager</div>

    <svg class="contact-icon icon-pin" viewBox="0 0 22 22" aria-hidden="true">
      <rect width="22" height="22" rx="2" fill="var(--accent-red)"/>
      <path d="M11 4a5 5 0 0 0-5 5c0 3.5 5 9 5 9s5-5.5 5-9a5 5 0 0 0-5-5z" fill="#fff"/>
      <circle cx="11" cy="9" r="2" fill="var(--accent-red)"/>
    </svg>
    <div class="contact-item address">Alder Crossing<br>Westmere Halden, 1742</div>

    <svg class="contact-icon icon-phone" viewBox="0 0 22 22" aria-hidden="true">
      <rect width="22" height="22" rx="2" fill="var(--accent-red)"/>
      <path d="M6 5l3 0 1 4-2 1.5a9 9 0 0 0 3.5 3.5L13 12l4 1v3a1 1 0 0 1-1 1A11 11 0 0 1 5 6a1 1 0 0 1 1-1z" fill="#fff"/>
    </svg>
    <div class="contact-item phone">02 5550 1928</div>

    <svg class="contact-icon icon-mobile" viewBox="0 0 22 22" aria-hidden="true">
      <rect width="22" height="22" rx="2" fill="var(--accent-red)"/>
      <rect x="7" y="4" width="8" height="14" rx="1.5" fill="#fff"/>
      <rect x="8.5" y="6" width="5" height="8" fill="var(--accent-red)"/>
    </svg>
    <div class="contact-item mobile">0491 570 156</div>

    <svg class="contact-icon icon-email" viewBox="0 0 22 22" aria-hidden="true">
      <rect width="22" height="22" rx="2" fill="var(--accent-red)"/>
      <rect x="4" y="6" width="14" height="10" fill="#fff"/>
      <path d="M4 6l7 5 7-5" fill="none" stroke="var(--accent-red)" stroke-width="1.5"/>
    </svg>
    <div class="contact-item email">contact@brightwell.com.au</div>

    <svg class="contact-icon icon-web" viewBox="0 0 22 22" aria-hidden="true">
      <rect width="22" height="22" rx="2" fill="var(--accent-red)"/>
      <circle cx="11" cy="11" r="6.5" fill="#fff"/>
      <path d="M4.5 11h13M11 4.5c-3 3.5-3 9.5 0 13M11 4.5c3 3.5 3 9.5 0 13" fill="none" stroke="var(--accent-red)" stroke-width="1.2"/>
    </svg>
    <div class="contact-item web">www.<span class="domain">learnroster</span>.com</div>

    <div class="brand-name">Wagely Allies</div>
  </div>
</div>
</body>
</html>
```